The Lantern Guide

I am a life coach specializing in helping people with depression and bipolar disorder. I would like a nice, fun design for a business card.

```html
<!DOCTYPE html>
<html lang="en">
<head>
<meta charset="utf-8">
<title>The Lantern Guide – Business Card</title>
<link rel="stylesheet" href="https://fonts.googleapis.com/css2?family=Montserrat:wght@700&family=Questrial&display=swap">
<style>
  :root {
    --panel-dark: #070908;
    --panel-light: #ffffff;
    --ink: #111111;
    --muted: #9aa3a2;
    --rule: #7f8c8b;
    --leaf: #7ed321;
  }
  * { margin: 0; padding: 0; box-sizing: border-box; }
  html, body { width: 1200px; height: 734px; overflow: hidden; background: var(--panel-light); }
  .card {
    position: relative;
    width: 1200px;
    height: 734px;
    background: var(--panel-light);
    font-family: "Questrial", "Century Gothic", sans-serif;
    overflow: hidden;
  }
  .card__dark-panel {
    position: absolute;
    left: 0; top: 0;
    width: 614px; height: 734px;
    background: var(--panel-dark);
  }
  .brand {
    position: absolute;
    left: 52px;
    top: 590px;
    display: flex;
    align-items: center;
    gap: 18px;
  }
  .brand__dot {
    width: 22px; height: 22px;
    border-radius: 50%;
    background: var(--leaf);
    flex: none;
  }
  .brand__name {
    font-family: "Montserrat", "Century Gothic", sans-serif;
    font-weight: 700;
    font-size: 44px;
    letter-spacing: 1px;
    color: var(--panel-light);
    text-transform: uppercase;
    white-space: nowrap;
  }
  .contact {
    position: absolute;
    left: 698px;
    top: 165px;
    height: 250px;
    border-left: 3px solid var(--rule);
    padding-left: 20px;
  }
  .contact__name {
    font-size: 46px;
    line-height: 1;
    color: var(--ink);
    margin-top: 2px;
  }
  .contact__role {
    font-size: 29px;
    line-height: 1.1;
    color: var(--muted);
  }
  .contact__details {
    list-style: none;
    margin-top: 68px;
    font-size: 29px;
    line-height: 34px;
    color: var(--muted);
  }
</style>
</head>
<body>
  <main class="card">
    <div class="card__dark-panel"></div>

    <div class="brand">
      <span class="brand__dot"></span>
      <span class="brand__name">The Lantern Guide</span>
    </div>

    <section class="contact">
      <h1 class="contact__name">Full Name</h1>
      <p class="contact__role">Your Position</p>
      <ul class="contact__details">
        <li>Telphone</li>
        <li>Email</li>
        <li>Address</li>
      </ul>
    </section>
  </main>
</body>
</html>
```